Veltrane Optics

I wish to make a mailing of a postcard format to pathologists in the UK. Probable number between 500 and 1000.There are 3 elements. 1. A small number of words (about 12) 2. A picture of our product 3. A relevant (tissue section) background. I have knocked up a rough idea of what I want ... BUT ... I'm obviously not a designer. The text looks awful and needs some way of standing out (and being legible) against the background. I can send original images of product and background. Important ... Aspect ratios of images must not be changed.

```html
<!DOCTYPE html>
<html lang="en">
<head>
<meta charset="utf-8">
<title>Veltrane Optics – Whole Slide Scanning Postcard</title>
<link rel="stylesheet" href="https://fonts.googleapis.com/css2?family=Alfa+Slab+One&family=Montserrat:wght@700&family=Playball&family=Sancreek&display=swap">
<style>
  :root {
    --page: #ffffff;
    --band-grey: #dcddde;
    --headline-red: #9b2423;
    --tissue-pink: #c2507f;
    --tissue-purple: #7a3f78;
    --tissue-light: #e7b3c8;
    --slab-yellow: #f6d27a;
    --cream: #eeeadb;
    --ink-shadow: #3a1626;
    --product-white: #eef0f1;
    --product-grey: #c9ccce;
    --label-dark: #2b2b2b;
    --white: #ffffff;
  }
  html, body {
    margin: 0;
    width: 1200px;
    height: 1000px;
    overflow: hidden;
    background: var(--page);
  }
  .postcard {
    position: absolute;
    left: 204px;
    top: 173px;
    width: 796px;
    height: 619px;
    overflow: hidden;
    box-shadow: 3px 4px 5px rgba(0,0,0,0.35);
    font-family: "Montserrat", sans-serif;
  }
  .header-band {
    position: absolute;
    inset: 0 0 auto 0;
    height: 184px;
    background: var(--band-grey);
  }
  .headline {
    position: absolute;
    margin: 0;
    color: var(--headline-red);
    font-weight: 700;
    font-size: 56px;
    line-height: 58px;
    letter-spacing: 0.3px;
  }
  .headline-main { left: 41px; top: 42px; }
  .headline-sub { left: 109px; top: 100px; }
  .tissue-background {
    position: absolute;
    left: 0; top: 184px;
    width: 796px; height: 435px;
    background:
      radial-gradient(ellipse 220px 160px at 720px 140px, var(--tissue-light), transparent 70%),
      radial-gradient(ellipse 300px 200px at 200px 300px, var(--tissue-purple), transparent 75%),
      linear-gradient(135deg, var(--tissue-pink), var(--tissue-purple) 55%, var(--tissue-pink));
  }
  .product-image {
    position: absolute;
    left: 436px; top: 128px;
    width: 326px; height: 275px;
    border-radius: 40px 40px 60px 30px;
    background: linear-gradient(160deg, var(--product-white), var(--product-grey));
  }
  .benefit {
    position: absolute;
    margin: 0;
    line-height: 1;
    text-shadow: 3px 3px 0 var(--ink-shadow), 0 0 8px rgba(40,10,25,0.6);
  }
  .benefit-compact {
    left: 44px; top: 200px;
    font-family: "Alfa Slab One", serif;
    font-size: 50px;
    letter-spacing: 2px;
    color: var(--slab-yellow);
  }
  .benefit-simple {
    left: 110px; top: 238px;
    font-family: "Playball", cursive;
    font-size: 88px;
    color: var(--cream);
  }
  .benefit-fast {
    left: 51px; top: 318px;
    font-family: "Alfa Slab One", serif;
    font-size: 54px;
    letter-spacing: 2px;
    color: var(--slab-yellow);
  }
  .benefit-affordable {
    left: 44px; top: 398px;
    font-family: "Sancreek", serif;
    font-size: 92px;
    color: var(--cream);
  }
  .web-address {
    position: absolute;
    left: 46px; top: 538px;
    padding: 2px 8px;
    background: rgba(190, 70, 120, 0.55);
    color: var(--white);
    font-weight: 700;
    font-size: 27px;
    letter-spacing: 0.5px;
  }
  .brand-box {
    position: absolute;
    left: 574px; top: 515px;
    width: 179px; height: 62px;
    background: var(--white);
    display: flex;
    align-items: center;
    justify-content: center;
    gap: 8px;
  }
  .brand-mark {
    width: 18px; height: 18px;
    background: var(--label-dark);
  }
  .brand-name {
    color: var(--label-dark);
    font-weight: 700;
    font-size: 19px;
  }
</style>
</head>
<body>
  <main class="postcard">
    <div class="header-band"></div>
    <h1 class="headline headline-main">Whole Slide Scanning</h1>
    <p class="headline headline-sub">is now...</p>

    <div class="tissue-background" role="img" aria-label="Stained tissue section micrograph in pink and purple"></div>

    <p class="benefit benefit-compact">COMPACT</p>
    <p class="benefit benefit-simple">Simple</p>
    <p class="benefit benefit-fast">FAST</p>
    <p class="benefit benefit-affordable">AFFORDABLE</p>

    <div class="product-image" role="img" aria-label="Photo of the compact white whole slide scanner"></div>

    <p class="web-address" style="margin:0">www.veltraneoptics.com</p>

    <div class="brand-box">
      <span class="brand-mark"></span>
      <span class="brand-name">Veltrane Optics</span>
    </div>
  </main>
</body>
</html>
```